Double sided flyer for industrial investment firm

We need a A4 double sided flyer (1 page, see attached draft), which we will fold in the midle. Text is attached. What is missing is a professional and clean looking design. Text length can not be changed. it is all in German, but that should not influence the design. The flyer is added to a letter which we send to small industrial companies as an introduction to us as an investor.

What is important?
- No fancy, colorful and funny designs.
- We want a clean, professional almost minimalist design. it does not take much design elements.
- Format either landscape or vertical, whatever works best.
- stay with the colors of our company (grey, blue). see www.velmora-ag.ch for details.
- Currently used graphic in the document should be used, but is not a must. Otherwise stay with pictures or Swiss Alps (if more pictures are needed). will upload some pictures as examples.

Format for the finished flyer: InDesign and Word document or similar.
Updates

The flyer will be folded in the middle so that it becomes A5. all current designs work only as a A4 format. An A4 folded has basically 4 pages, each being A5 size. Please adapt the design accordingly.

Target Market(s)

Owners of small to medium industrial companies in Switzerland

Industry/Entity Type

Industrial

Font styles to use
Serif
Sans Serif

Colors
0255a3
3276b5
85abd2
cedeed

Requirements
Must have
• 1 page, double sided. folded in the middle. A4 Format

```html
<!DOCTYPE html>
<html lang="de">
<head>
<meta charset="utf-8">
<title>Velmora AG – Faltflyer Innenseiten</title>
<link href="https://fonts.googleapis.com/css2?family=Open+Sans:wght@400;600;700&display=swap" rel="stylesheet">
<style>
  :root {
    --bg: #e9e9e9;
    --paper: #ffffff;
    --band-dark: #3c3c3c;
    --band-dark-2: #595959;
    --band-mid: #6e6e6e;
    --band-mid-2: #8a8a8a;
    --ink: #2b2b2b;
    --ink-soft: #5a5a5a;
    --on-dark: #f2f2f2;
    --photo: #9a9a9a;
    --fold: rgba(0,0,0,0.18);
  }
  * { box-sizing: border-box; margin: 0; padding: 0; }
  html, body { width: 1200px; height: 1000px; overflow: hidden; }
  body {
    background: radial-gradient(ellipse at 50% 40%, #f7f7f7 0%, var(--bg) 70%, #dcdcdc 100%);
    font-family: "Open Sans", Arial, sans-serif;
    display: flex; align-items: center; justify-content: center;
  }
  .spread {
    width: 1100px; height: 778px;
    display: flex; position: relative;
    background: var(--paper);
    box-shadow: 0 14px 40px rgba(0,0,0,0.22);
  }
  .spread::after {
    content: ""; position: absolute; top: 0; bottom: 0; left: 520px; width: 60px;
    background: linear-gradient(90deg, transparent, var(--fold) 50%, transparent);
    pointer-events: none;
  }
  .page {
    width: 550px; height: 100%;
    display: flex; flex-direction: column;
    padding: 18px; gap: 10px;
  }
  .section {
    flex: 1; padding: 14px 18px;
    display: flex; flex-direction: column; gap: 6px;
  }
  .section h2 {
    font-size: 16px; font-weight: 700; line-height: 1.25;
  }
  .section p {
    font-size: 12.5px; line-height: 1.55;
  }
  .section--dark {
    background: linear-gradient(180deg, var(--band-dark-2), var(--band-dark));
    color: var(--on-dark);
  }
  .section--mid {
    background: linear-gradient(180deg, var(--band-mid-2), var(--band-mid));
    color: var(--on-dark);
  }
  .section--light {
    background: var(--paper);
    color: var(--ink);
    border: 1px solid #d4d4d4;
  }
  .section--light p { color: var(--ink-soft); }
  .section--team { flex-direction: row; gap: 14px; align-items: flex-start; }
  .team-text { flex: 1; display: flex; flex-direction: column; gap: 6px; }
  .team-photos { display: flex; gap: 6px; }
  .team-photo {
    width: 58px; height: 74px;
    background: linear-gradient(180deg, #b5b5b5, var(--photo));
  }
</style>
</head>
<body>
  <main class="spread">
    <section class="page page--left">
      <article class="section section--dark">
        <h2>Wer sind wir?</h2>
        <p>Wir sind eine unabhängige Schweizer Beteiligungsgesellschaft, die sich langfristig an kleinen und mittleren Industrieunternehmen beteiligt. Unsere Partner bringen langjährige Erfahrung aus Industrie, Finanzwesen und Unternehmensführung mit.</p>
      </article>
      <article class="section section--light">
        <h2>Was ist unser Ziel/Vision?</h2>
        <p>Wir wollen gesunde Unternehmen mit ihren Mitarbeitenden erhalten und gemeinsam mit dem Management weiterentwickeln. Dabei steht nicht der schnelle Gewinn, sondern nachhaltiges Wachstum im Vordergrund.</p>
      </article>
      <article class="section section--mid">
        <h2>Welches Kapital investieren wir?</h2>
        <p>Wir investieren ausschliesslich eigenes Kapital unserer Partner und Aktionäre. Dadurch sind wir frei von festen Laufzeiten und können Entscheidungen rasch und unabhängig treffen.</p>
      </article>
      <article class="section section--light">
        <h2>Wie arbeiten wir?</h2>
        <p>Wir begleiten die Unternehmen aktiv im Verwaltungsrat und unterstützen das Management bei strategischen Fragen. Das operative Tagesgeschäft bleibt in den bewährten Händen vor Ort.</p>
      </article>
      <article class="section section--dark">
        <h2>Wie unterscheiden wir uns von einem Private Equity Fund?</h2>
        <p>Im Gegensatz zu einem Fonds müssen wir unsere Beteiligungen nicht nach wenigen Jahren wieder verkaufen. Wir denken in Generationen und bleiben ein verlässlicher Partner für Eigentümer und Belegschaft.</p>
      </article>
    </section>

    <section class="page page--right">
      <article class="section section--dark">
        <h2>Wie investieren wir?</h2>
        <p>Wir übernehmen Mehrheits- oder Minderheitsbeteiligungen, häufig im Rahmen einer Nachfolgeregelung. Die Struktur jeder Transaktion wird individuell auf die Bedürfnisse des Verkäufers abgestimmt.</p>
      </article>
      <article class="section section--light section--team">
        <div class="team-text">
          <h2>Wer ist unser Management?</h2>
          <p>Unser Team besteht aus drei Partnern mit fundierter Erfahrung in der Führung von Industriebetrieben und in der Begleitung von Unternehmensnachfolgen.</p>
        </div>
        <div class="team-photos">
          <div class="team-photo" role="img" aria-label="Porträtfoto Partner 1"></div>
          <div class="team-photo" role="img" aria-label="Porträtfoto Partner 2"></div>
          <div class="team-photo" role="img" aria-label="Porträtfoto Partner 3"></div>
        </div>
      </article>
      <article class="section section--mid">
        <h2>Wie sind unsere Investoren eingebunden?</h2>
        <p>Unsere Investoren sind erfahrene Unternehmer aus der Schweiz. Sie stellen ihr Wissen und ihr Netzwerk den Beteiligungen zur Verfügung, wann immer dies gewünscht wird.</p>
      </article>
      <article class="section section--light">
        <h2>Wie entscheiden wir?</h2>
        <p>Entscheide fallen schnell und transparent. Nach einem ersten Gespräch erhalten Sie innert weniger Wochen eine klare Rückmeldung zu unserem Interesse und den nächsten Schritten.</p>
      </article>
      <article class="section section--dark">
        <h2>Welche Unternehmen sucht die Velmora AG?</h2>
        <p>Wir suchen profitable Industrieunternehmen in der Schweiz mit einem Umsatz zwischen fünf und fünfzig Millionen Franken, einer starken Marktstellung und motivierten Mitarbeitenden.</p>
      </article>
    </section>
  </main>
</body>
</html>
```